Asia based real estate financing firm needs and AWESOME design for a biz card -Harbor Lending Circle

Looking for a stylish, & corporate-looking business card for a real estate financing brokerage firm in Asia, offering global mortgage loans. I uploaded our current logos. We would like to add a splash of color (perhaps the house icon) or any other suggestions are open. For the winning designer, we have a lot of work! Thanks and best of luck!

Target Market(s)

Real estate investors globally. We want to look more like a BANK and NOT a real estate company. Please don't play up on a "house" design.

Industry/Entity Type

Banking

Contact Information for Business Card

Harbor Lending Circle
Peter Wilks
Co-Founder | Partner

14 Cassia Lane, Suite 310
Singapore 047219
www.hlc-example.asia
peterwilks@hlc-example.asia
+65 555-0142
WeChat: peterwilks

Colors

Designer to choose colors to be used in the design.

Requirements
Must have
• Must have the standard business requirements for a card; name, address, email, etc
• Can be horizontal or vertical.
Nice to have
• It would be great to see some sort of variation to the logo with a pop of color. Red is good as we're in Asia, however, other options work as well.
• Our tag line is - Borderless mortgages. It doesn't have to be on the card but might be nice.
• I'd like to start seeing our tagline within the cards as well. - Borderless mortgages.
• Also, please add our location. The location for this card is Singapore so perhaps it can be highlighted or emphasised in some way.
• Singapore | Hong Kong | Shanghai | Manila
• As we will soon open an office in Shanghai, having an option for both languages would be great.
Should not have
• I'm exceited and open to your creativity ... knock it out of the park!

```html
<!DOCTYPE html>
<html lang="en">
<head>
<meta charset="utf-8">
<title>Harbor Lending Circle – Business Card</title>
<link href="https://fonts.googleapis.com/css2?family=Cinzel:wght@400;700&family=Open+Sans:wght@400&display=swap" rel="stylesheet">
<style>
  :root {
    --backdrop: #999999;
    --card-dark: #000000;
    --card-light: #ffffff;
    --ink-light: #ffffff;
    --ink-dark: #111111;
    --divider: #3a3a3a;
    --shadow: rgba(0,0,0,0.45);
  }
  * { margin: 0; padding: 0; box-sizing: border-box; }
  html, body {
    width: 1200px; height: 900px; overflow: hidden;
    background: var(--backdrop);
  }
  .stage { position: relative; width: 1200px; height: 900px; }

  .card {
    position: absolute;
    box-shadow: 3px 4px 6px var(--shadow);
  }
  .card--front {
    left: 120px; top: 275px; width: 478px; height: 295px;
    background: var(--card-dark);
    border-radius: 0 52px 0 52px;
    color: var(--ink-light);
  }
  .card--back {
    left: 606px; top: 275px; width: 477px; height: 292px;
    background: var(--card-light);
    border-radius: 52px 0 52px 0;
    color: var(--ink-dark);
  }

  .wordmark {
    position: absolute;
    font-family: 'Cinzel', serif;
    font-weight: 400;
    text-align: center;
    line-height: 1.25;
    letter-spacing: 0.04em;
  }
  .card--front .wordmark {
    left: 20px; top: 112px; width: 200px;
    font-size: 17px;
    color: var(--ink-light);
  }
  .card--back .wordmark {
    left: 0; top: 108px; width: 477px;
    font-size: 25px;
    color: var(--ink-dark);
  }

  .divider {
    position: absolute;
    left: 238px; top: 70px; width: 1px; height: 148px;
    background: var(--divider);
  }

  .details {
    position: absolute;
    left: 258px; top: 66px;
    font-family: 'Open Sans', sans-serif;
    font-size: 13.5px;
    line-height: 17px;
  }
  .details__name {
    font-family: 'Cinzel', serif;
    font-weight: 700;
    font-size: 19px;
    line-height: 22px;
    letter-spacing: 0.02em;
  }
  .details__title { margin-bottom: 6px; }
  .contact-list { list-style: none; margin-bottom: 7px; }
  .contact-list li { display: flex; align-items: center; gap: 5px; }
  .contact-list svg { width: 11px; height: 11px; flex: none; fill: var(--ink-light); }
</style>
</head>
<body>
<div class="stage">

  <section class="card card--front">
    <div class="wordmark">Harbor Lending<br>Circle</div>
    <div class="divider"></div>
    <div class="details">
      <div class="details__name">PETER WILKS</div>
      <div class="details__title">Co-Founder | Partner</div>
      <ul class="contact-list">
        <li>
          <svg viewBox="0 0 12 12" aria-hidden="true"><path d="M1 3.5 Q6 0 11 3.5 L9.5 5 L8 4 L8 3 Q6 2.4 4 3 L4 4 L2.5 5 Z M3 6 H9 L10.5 10 H1.5 Z"/></svg>
          +65 555-0142
        </li>
        <li>
          <svg viewBox="0 0 12 12" aria-hidden="true"><rect x="0.5" y="2.5" width="11" height="7"/><path d="M0.5 2.5 L6 6.5 L11.5 2.5" fill="none" stroke="#000" stroke-width="1"/></svg>
          peterwilks@hlc-example.asia
        </li>
        <li>
          <svg viewBox="0 0 12 12" aria-hidden="true"><circle cx="6" cy="6" r="5.5"/><path d="M3 4 Q5 3 5.5 5 Q4 7 5 9 M7 3 Q9 4 8.5 6" fill="none" stroke="#000" stroke-width="1"/></svg>
          www.hlc-example.asia
        </li>
        <li>
          <svg viewBox="0 0 12 12" aria-hidden="true"><circle cx="6" cy="6" r="5.5"/></svg>
          peterwilks
        </li>
      </ul>
      <div class="details__address">14 Cassia Lane, Suite 310<br>Singapore 047219</div>
    </div>
  </section>

  <section class="card card--back">
    <div class="wordmark">Harbor Lending<br>Circle</div>
  </section>

</div>
</body>
</html>
```